Larkwell Moments Studio Website
looking for wow/drama
Larkwell Moments Studio Website - Events
Creative Brief
Events
www.larkwellmoments.example
Based in Greater Boston, Larkwell Moments Studio is a boutique custom events and marketing firm.
Looking for dramatic layout/bold. Clean and simple...DRAMA/showstopper! I like texture would prefer navigation to be unique - located in a new place/different layout -- unexpected I WANT A VERY UNIQUE LAYOUT Don't like: anything ordinary/hate wehn things feel "flat"
Black
Teal (the exact teal of my logo)
White and dark Grey accents (from my logo)
right side
http://www.doranpeswick.example/
http://www.thebrightorchard.example/
http://www.velvetaffairs.example.uk/
drama wins. I will not have much "copy" cluttering up my website, The look of the website needs to be a showstopper. other websites: http://www.zintrova.example.uk/ (unique layout) http://www.quillmarshband.example.uk/index4.php http://www.brantoloft.example/

```html
<!DOCTYPE html>
<html lang="en">
<head>
<meta charset="utf-8">
<title>Larkwell Moments Studio</title>
<link rel="stylesheet" href="https://fonts.googleapis.com/css2?family=Cinzel:wght@400&family=Open+Sans:wght@400;600&display=swap">
<style>
  :root {
    --teal: #2ad1cf;
    --teal-bright: #5ff0ec;
    --teal-deep: #0f4f50;
    --teal-dark: #082829;
    --black: #000000;
    --white: #f4fbfb;
    --grey: #9aa9a9;
    --grey-dark: #2c3333;
  }
  * { margin: 0; padding: 0; box-sizing: border-box; }
  html, body {
    width: 1200px; height: 845px; overflow: hidden;
    background: var(--black);
  }
  .page {
    position: relative; width: 1200px; height: 845px; overflow: hidden;
    background: linear-gradient(180deg, var(--teal-dark) 0%, #061c1d 45%, #020707 68%, var(--black) 80%);
    color: var(--white);
    font-family: "Open Sans", Arial, sans-serif;
  }
  .top-band {
    position: absolute; top: 0; left: 0; width: 1200px; height: 12px;
    background: linear-gradient(180deg, var(--teal-bright), var(--teal) 60%, var(--teal-deep));
  }
  .texture {
    position: absolute; top: 12px; left: 0; width: 1200px; height: 640px;
    background:
      radial-gradient(ellipse 330px 260px at 600px 90px, rgba(95,240,236,0.85), rgba(42,209,207,0.45) 40%, rgba(15,79,80,0.25) 75%, rgba(15,79,80,0) 100%),
      radial-gradient(ellipse 700px 420px at 600px 200px, rgba(20,90,92,0.55), rgba(8,40,41,0) 100%),
      linear-gradient(180deg, rgba(0,0,0,0) 55%, rgba(0,0,0,0.9) 100%);
  }
  .masthead {
    position: absolute; top: 180px; left: 0; width: 1200px; text-align: center;
  }
  .brand-name {
    font-family: "Cinzel", "Times New Roman", serif;
    font-weight: 400; font-size: 44px; letter-spacing: 2px;
    color: var(--white);
  }
  .tagline {
    margin-top: 22px;
    font-family: "Cinzel", "Times New Roman", serif;
    font-size: 22px; letter-spacing: 1px; color: var(--white);
  }
  .intro {
    width: 470px; margin: 16px auto 0;
    font-size: 10.5px; line-height: 14px; color: #d8e6e6;
  }
  .more-link {
    display: inline-block; margin-top: 14px;
    font-size: 10.5px; font-weight: 600; color: var(--white); text-decoration: none;
  }
  .more-link::before { content: "| "; color: var(--grey); }
  .main-nav {
    position: absolute; top: 502px; left: 0; width: 1200px;
    display: flex; justify-content: center; align-items: center; gap: 18px;
    font-family: "Cinzel", "Times New Roman", serif; font-size: 25px;
  }
  .main-nav a { color: var(--white); text-decoration: none; position: relative; }
  .nav-divider { color: var(--grey); font-family: "Open Sans", Arial, sans-serif; font-size: 16px; }
  .main-nav .current svg { position: absolute; left: 10px; top: 38px; }
  .footer-mark {
    position: absolute; top: 720px; left: 0; width: 1200px; text-align: center;
    font-family: "Cinzel", "Times New Roman", serif; font-size: 20px; color: var(--grey-dark);
  }
  .copyright {
    position: absolute; top: 774px; left: 0; width: 1200px; text-align: center;
    font-size: 10px; color: var(--grey-dark);
  }
</style>
</head>
<body>
<div class="page">
  <div class="top-band"></div>
  <div class="texture" role="img" aria-label="Teal damask pattern with a glowing floral ornament behind the studio name"></div>

  <header class="masthead">
    <h1 class="brand-name">Larkwell Moments Studio</h1>
    <p class="tagline">Custom Events &amp; Marketing</p>
    <p class="intro">Lorem ipsum dolor sit amet, consectetur adipisicing elit, sed do eiusmod tempor incididunt ut labore et dolore magna aliqua. Ut enim ad minim veniam, quis nostrud exercitation ullamco laboris nisi ut aliquip ex ea commodo consequat. Duis aute irure dolor in reprehenderit in voluptate velit esse cillum dolore eu fugiat nulla pariatur. Excepteur sint occaecat cupidatat non proident, sunt in culpa qui officia deserunt mollit anim id est laborum modo consequat.</p>
    <a class="more-link" href="#">more details</a>
  </header>

  <nav class="main-nav">
    <a href="#">Home</a>
    <span class="nav-divider">|</span>
    <a href="#" class="current">Business Services
      <svg width="180" height="12" viewBox="0 0 180 12" aria-hidden="true">
        <path d="M2 10 Q90 -2 178 10" fill="none" stroke="#2ad1cf" stroke-width="2"/>
      </svg>
    </a>
    <span class="nav-divider">|</span>
    <a href="#">Home Gatherings</a>
    <span class="nav-divider">|</span>
    <a href="#">Contact LMS</a>
  </nav>

  <div class="footer-mark">Larkwell Moments Studio</div>
  <p class="copyright">All rights reserved. ©2011 Larkwell Moments Studio</p>
</div>
</body>
</html>
```